Criação de Papelaria Profissional para Imóveis
A empresa queria:
" Eu sou conhecido no seguimento . Atuo no meio e alto padrão. Vendo Para as construtoras e revendas . Lotes e casas "

```html
<!DOCTYPE html>
<html lang="pt-BR">
<head>
<meta charset="UTF-8">
<title>Assinatura de E-mail — Vallore Imóveis</title>
<link href="https://fonts.googleapis.com/css2?family=Montserrat:wght@400;600;700;800&display=swap" rel="stylesheet">
<style>
  :root {
    --page-bg: #e9eaec;
    --navy-deep: #0b1733;
    --navy-mid: #1a2c55;
    --navy-text: #1d2d56;
    --panel-text: #ffffff;
    --ink-soft: #5a6275;
    --card: #ffffff;
  }
  * { margin: 0; padding: 0; box-sizing: border-box; }
  html, body {
    width: 1200px;
    height: 1200px;
    overflow: hidden;
  }
  body {
    background: var(--page-bg);
    font-family: "Montserrat", sans-serif;
    display: flex;
    align-items: center;
    justify-content: center;
  }
  .signature {
    width: 1080px;
    background: var(--card);
    padding: 40px;
    display: flex;
    align-items: center;
    gap: 44px;
  }
  .brand-panel {
    width: 470px;
    height: 210px;
    flex-shrink: 0;
    background: linear-gradient(100deg, var(--navy-deep) 0%, var(--navy-mid) 100%);
    display: flex;
    align-items: center;
    justify-content: center;
  }
  .brand-name {
    display: flex;
    align-items: center;
    gap: 18px;
    font-size: 48px;
    font-weight: 700;
    letter-spacing: 3px;
    color: var(--panel-text);
    line-height: 1;
  }
  .brand-square {
    width: 30px;
    height: 30px;
    background: var(--panel-text);
  }
  .contact-block {
    flex: 1;
    display: flex;
    flex-direction: column;
    gap: 26px;
  }
  .person { width: max-content; }
  .person-name {
    font-size: 30px;
    color: var(--navy-text);
    letter-spacing: 0.5px;
  }
  .person-name strong { font-weight: 800; }
  .person-name span { font-weight: 400; }
  .person-role {
    text-align: right;
    font-size: 13px;
    font-weight: 700;
    color: var(--navy-text);
    letter-spacing: 1px;
    margin-top: 2px;
  }
  .details {
    display: flex;
    gap: 46px;
  }
  .detail-column { display: flex; flex-direction: column; gap: 18px; }
  .detail-row {
    display: flex;
    align-items: flex-start;
    gap: 14px;
    font-size: 14px;
    line-height: 1.45;
    color: var(--ink-soft);
  }
  .detail-row svg { flex-shrink: 0; margin-top: 3px; }
  .detail-row.address { margin-top: 28px; }
</style>
</head>
<body>
  <section class="signature">
    <div class="brand-panel">
      <div class="brand-name"><span class="brand-square"></span>VALLORE</div>
    </div>

    <div class="contact-block">
      <div class="person">
        <div class="person-name"><strong>NOME</strong> <span>SOBRENOME</span></div>
        <div class="person-role">CARGO - FUNÇÃO</div>
      </div>

      <div class="details">
        <div class="detail-column">
          <div class="detail-row">
            <svg width="20" height="20" viewBox="0 0 24 24" aria-hidden="true">
              <path fill="var(--navy-text)" d="M6.6 10.8a15.2 15.2 0 0 0 6.6 6.6l2.2-2.2a1 1 0 0 1 1-.25 11.4 11.4 0 0 0 3.6.57 1 1 0 0 1 1 1V20a1 1 0 0 1-1 1A17 17 0 0 1 3 4a1 1 0 0 1 1-1h3.5a1 1 0 0 1 1 1c0 1.25.2 2.45.57 3.6a1 1 0 0 1-.25 1z"/>
            </svg>
            <div>+55 (11) 99999-9999<br>+55 (11) 99999-9999</div>
          </div>
          <div class="detail-row">
            <svg width="20" height="20" viewBox="0 0 24 24" aria-hidden="true">
              <circle cx="12" cy="12" r="9" fill="none" stroke="var(--navy-text)" stroke-width="2"/>
              <path d="M3 12h18M12 3c3 3.2 3 14.8 0 18M12 3c-3 3.2-3 14.8 0 18" fill="none" stroke="var(--navy-text)" stroke-width="1.6"/>
            </svg>
            <div>email@seuemail.com.br<br>www.site.com.br</div>
          </div>
        </div>

        <div class="detail-column">
          <div class="detail-row address">
            <svg width="18" height="22" viewBox="0 0 24 30" aria-hidden="true">
              <path fill="var(--navy-text)" d="M12 0C5.4 0 0 5.3 0 11.8 0 20.6 12 30 12 30s12-9.4 12-18.2C24 5.3 18.6 0 12 0zm0 16.5a4.7 4.7 0 1 1 0-9.4 4.7 4.7 0 0 1 0 9.4z"/>
            </svg>
            <div>Rua Exemplo de Nome, 1111<br>Bairro Nome do Bairro<br>88888-000 - São Paulo / SP</div>
          </div>
        </div>
      </div>
    </div>
  </section>
</body>
</html>
```